Lena Business card

This card is to represent me as a coach and Vivamora facilitator
Double sided in colour
A beautiful, simple and elegant design that indicates movement and is modern, FRESH and uplifting. Please don’t use much black and use the attached Vivamora logo.
Preferred colours - white, lighter blues and fresh greens

Target Market(s)
Business people - potential clients age 35 up
Industry/Entity Type
Business
Requirements
Must have
-  Text for the front :
Lumivera Living
Lena Darrow
Biocentric Coach
Co-Director, Vivamora School of Australia
E: lena@vivamora.com.au
M: 0471 552 908.
W: vivamora.com.au
Biocentric Coaching for Individuals, Teams and Organisations
Vivamora for Children, Adults and Social development projects
Text for the back :
The Vivamora system facilitates the expression of human potential for health, happiness and humanity through music, movement and group interaction. It was developed by Emilio Vasca Orduña, a Chilean anthropologist and clinical psychologist, in 1976.
Creative use of the logo - integrating it within the design - e.g perhaps using it as the O in Vivamora,
Please feature the heron from the logo or a another elegant graceful stylized heron.

```html
<!DOCTYPE html>
<html lang="en">
<head>
<meta charset="utf-8">
<title>Lena Darrow – Business Card</title>
<link rel="stylesheet" href="https://fonts.googleapis.com/css2?family=Questrial&display=swap">
<style>
  :root {
    --page: #ecebe8;
    --card: #fbfbfa;
    --ink: #2e2e2e;
    --ink-soft: #4a4a4a;
    --sky: #9cc6dc;
    --sky-soft: #b7d6e6;
    --tagline: #a8c9da;
    --heron: #eab49c;
    --heron-deep: #e29c80;
  }
  * { box-sizing: border-box; margin: 0; padding: 0; }
  html, body {
    width: 1200px;
    height: 417px;
    overflow: hidden;
    background: var(--page);
    font-family: "Questrial", "Century Gothic", sans-serif;
    color: var(--ink);
  }
  .sheet {
    position: relative;
    width: 1200px;
    height: 417px;
  }
  .card {
    position: absolute;
    top: 48px;
    width: 560px;
    height: 320px;
    background: var(--card);
    overflow: hidden;
    box-shadow: 0 2px 6px rgba(0,0,0,0.12);
  }
  .card--back { left: 26px; }
  .card--front { left: 614px; }

  /* Back side */
  .heron-art {
    position: absolute;
    inset: 0;
    width: 100%;
    height: 100%;
  }
  .about {
    position: absolute;
    left: 38px;
    right: 38px;
    top: 192px;
    font-size: 13px;
    line-height: 1.5;
    font-style: italic;
    text-align: center;
    color: var(--ink);
  }

  /* Front side */
  .brand-name {
    position: absolute;
    left: 18px;
    top: 20px;
    font-size: 32px;
    line-height: 1;
    color: var(--ink);
  }
  .taglines {
    position: absolute;
    left: 18px;
    top: 66px;
    font-size: 11.5px;
    line-height: 1.45;
    text-transform: uppercase;
    color: var(--tagline);
    letter-spacing: 0.2px;
  }
  .person {
    position: absolute;
    left: 18px;
    top: 124px;
    font-size: 16px;
    line-height: 1.45;
  }
  .person__role { font-style: italic; }
  .contact {
    position: absolute;
    left: 18px;
    top: 190px;
    font-size: 15px;
    line-height: 1.5;
    list-style: none;
    color: var(--ink-soft);
  }
  .wave {
    position: absolute;
    left: 0;
    bottom: 0;
    width: 560px;
    height: 130px;
  }
</style>
</head>
<body>
<main class="sheet">

  <section class="card card--back" aria-label="Card back">
    <svg class="heron-art" viewBox="0 0 560 320">
      <defs>
        <radialGradient id="heronTone" cx="50%" cy="45%" r="60%">
          <stop offset="0%" stop-color="#e29c80" stop-opacity="0.55"/>
          <stop offset="100%" stop-color="#eab49c" stop-opacity="0.15"/>
        </radialGradient>
      </defs>
      <g role="img" aria-label="Large stylised heron in flight, drawn in soft coral line work">
        <ellipse cx="160" cy="150" rx="150" ry="145" fill="url(#heronTone)"/>
      </g>
      <g role="img" aria-label="Small stylised heron in flight, coral line work">
        <ellipse cx="488" cy="60" rx="58" ry="55" fill="url(#heronTone)"/>
      </g>
    </svg>
    <p class="about">The Vivamora system facilitates the expression of human potential for health, happiness and humanity through music, movement and group interaction. It was developed by Emilio Vasca Orduña, a Chilean anthropologist and clinical psychologist, in 1976.</p>
  </section>

  <section class="card card--front" aria-label="Card front">
    <p class="brand-name">Lumivera Living</p>
    <p class="taglines">
      Biocentric coaching for individuals, teams and organisations<br>
      Vivamora for children, adults and social development projects
    </p>
    <div class="person">
      <p class="person__name">Lena Darrow - Biocentric Coach</p>
      <p class="person__role">Co-Director, Vivamora School of Australia</p>
    </div>
    <ul class="contact">
      <li>E: lena@vivamora.com.au</li>
      <li>M: 0471 552 908</li>
      <li>W: vivamora.com.au</li>
    </ul>
    <svg class="wave" viewBox="0 0 560 130" preserveAspectRatio="none" aria-hidden="true">
      <path d="M0 96 C 180 92, 380 60, 560 6 L560 130 L0 130 Z" fill="#b7d6e6"/>
    </svg>
  </section>

</main>
</body>
</html>
```